Renewed electronic office supplies

I need a landing page design for a B2B business that will sell refurbished and renewed electronic devices such as smartphones, laptops, tablets and other gadgets. We want to become suppliers of these devices to companies that need computers and other devices for their employees. The point of our business is that they can get a great device that is in very good contrition instead of buying brand new. Companies will be able to save 50-60% on these renewed devices. Not only that we will also buy the companies old devices which they no longe needs and renew them and give them new life so we can resell it.

Our services will be:

- sale of renewed devices with lifetime warranty

- purchase of old devices

- swap solution: meaning client buy from us and sell at the same time so we deduct the amount sale of their old devices into their purchase.

Some useful information:

- company name and logo are still pending

- we aim to provide all business with top quality of renewed and environmentally friendly electronics, while maintaining a minimal impact on the natural environment.

I have attached a word document with some additional info that might be useful

Looking forward to seeing all your great designs!

P.s. Please feel free to make designs that are not based on my documents also, we need different layouts and designs. as for now I see many of the designs are more or less the same. we need more variation on design

Target Market(s)

Medium to large Businesses

Industry/Entity Type

Technology Equipment

Requirements
Must have
• we need more designs to be submitted , 50 designs minimum

```html
<!DOCTYPE html>
<html lang="en">
<head>
<meta charset="utf-8">
<title>Renewpoint Supply – Reusable Electronic Office Supplies</title>
<link rel="stylesheet" href="https://fonts.googleapis.com/css2?family=Montserrat:wght@400;600;700;800&family=Open+Sans:wght@400;600;700&display=swap">
<style>
  :root{
    --purple-deep:#2c1a6e;
    --purple:#5a2a96;
    --magenta:#b52f82;
    --blue:#27a3e8;
    --blue-soft:#d8ecfb;
    --navy:#13184a;
    --ink:#1c1c2b;
    --text:#6d7080;
    --white:#ffffff;
  }
  *{box-sizing:border-box;margin:0;padding:0}
  html,body{width:1200px;height:3048px;overflow:hidden}
  body{position:relative;background:var(--white);font-family:"Open Sans",Arial,sans-serif;color:var(--ink)}
  .abs{position:absolute}
  h1,h2,h3,.brand,.nav a,.btn{font-family:"Montserrat",Arial,sans-serif}

  /* Hero */
  .hero-bg{left:0;top:0;width:1200px;height:720px}
  .brand{left:140px;top:30px;color:var(--white);font-weight:600;font-size:25px;line-height:30px}
  .nav{right:170px;top:48px;display:flex;gap:22px}
  .nav a{color:var(--white);text-decoration:none;font-size:13px;font-weight:600}
  .nav a.active{border-bottom:2px solid var(--white);padding-bottom:4px}
  .hero-title{left:140px;top:204px;width:620px;color:var(--white);font-weight:800;font-size:41px;line-height:50px}
  .hero-text{left:140px;top:336px;width:460px;color:#e7dcf4;font-size:14px;line-height:24px}
  .btn{display:inline-flex;align-items:center;gap:8px;background:var(--blue);color:var(--white);border-radius:30px;font-weight:700;text-transform:uppercase}
  .hero-btn{left:140px;top:478px;height:42px;padding:0 22px;font-size:13px}
  .dots{left:140px;top:604px;display:flex;gap:8px}
  .dots span{width:9px;height:9px;border-radius:50%;background:rgba(255,255,255,.55)}
  .dots span:first-child{background:var(--white)}
  .hero-phone{left:800px;top:-40px;width:300px;height:600px;border-radius:44px;transform:rotate(14deg);background:linear-gradient(160deg,#1d1d2a 0%,#2b2f6e 30%,#d4366b 62%,#f28a3f 82%,#3ab7f0 100%);box-shadow:0 30px 60px rgba(20,10,60,.45);border:10px solid #15151e}

  /* Decorative blobs */
  .blob{border-radius:50%;background:var(--blue-soft)}

  /* Categories */
  .cat{top:790px;width:262px;height:300px;border-radius:16px;overflow:hidden}
  .cat-photo{width:100%;height:100%}
  .cat-label{position:absolute;left:0;right:0;bottom:26px;text-align:center;color:var(--white);font-family:"Montserrat",Arial,sans-serif;font-weight:700;font-size:19px}

  /* We are */
  .we-title{left:140px;top:1180px;font-size:50px;font-weight:800;color:var(--ink)}
  .we-sub{left:140px;top:1262px;font-family:"Montserrat",Arial,sans-serif;font-size:17px;font-weight:700;color:#2c56b8}
  .we-text{left:140px;top:1306px;width:470px;font-size:12px;line-height:21px;color:var(--text)}
  .feature{left:140px;width:470px;display:flex;gap:22px}
  .feature-icon{flex:none;width:56px;height:56px;border-radius:50%;display:flex;align-items:center;justify-content:center;color:var(--white);font-weight:700;font-size:26px}
  .feature h3{font-size:19px;font-weight:700;margin:4px 0 8px}
  .feature p{font-size:12px;line-height:21px;color:var(--text)}
  .device{top:1236px;width:195px;height:360px;border-radius:34px;border:9px solid #1b1b22;box-shadow:0 20px 40px rgba(0,0,30,.25)}

  /* Services */
  .services-title{left:0;top:1958px;width:1200px;text-align:center;font-size:50px;font-weight:800}
  .service{width:420px;display:flex;gap:34px}
  .service-icon{flex:none;width:150px;height:150px;position:relative}
  .service h3{font-size:17px;font-weight:700;line-height:22px;margin-top:6px;width:220px}
  .service p{font-size:11.5px;line-height:19px;color:var(--text);margin:12px 0 14px;width:230px}
  .read{height:30px;padding:0 16px;font-size:10px}

  /* Footer */
  .footer-bg{left:0;top:2580px;width:1200px;height:468px}
  .subscribe{left:150px;top:2752px;color:var(--white);font-family:"Montserrat",Arial,sans-serif;font-weight:700;font-size:21px}
  .sub-form{left:590px;top:2740px;width:470px;height:50px;background:var(--white);border-radius:30px;display:flex;align-items:center;justify-content:space-between;padding:0 6px 0 22px}
  .sub-form span{color:#8a8da0;font-size:13px}
  .sub-form .btn{height:38px;padding:0 18px;font-size:11px}
  .social{left:0;top:2862px;width:1200px;display:flex;justify-content:center;gap:14px}
  .social span{width:36px;height:36px;border-radius:50%;border:1.5px solid rgba(255,255,255,.8)}
  .foot-nav{left:0;top:2936px;width:1200px;display:flex;justify-content:center;gap:42px}
  .foot-nav a{color:var(--white);text-decoration:none;font-family:"Montserrat",Arial,sans-serif;font-weight:700;font-size:16px}
  .copyright{left:0;top:3000px;width:1200px;text-align:center;color:#b9bcd6;font-size:11px}
</style>
</head>
<body>

<!-- Hero -->
<svg class="abs hero-bg" viewBox="0 0 1200 720" aria-hidden="true">
  <defs>
    <linearGradient id="heroGrad" x1="0" y1="0" x2="1" y2="1">
      <stop offset="0" stop-color="#2a1b70"/>
      <stop offset=".55" stop-color="#6a2a98"/>
      <stop offset="1" stop-color="#c5347f"/>
    </linearGradient>
  </defs>
  <path d="M0 0H1200V560C1000 620 760 700 460 700 260 700 110 690 0 672Z" fill="url(#heroGrad)"/>
  <path d="M0 672C110 690 260 700 460 700 760 700 1000 620 1200 560V590C1000 650 760 716 460 716 260 716 110 706 0 690Z" fill="var(--blue)"/>
</svg>
<div class="abs hero-phone" role="img" aria-label="Photo of a renewed smartphone with a colourful screen"></div>
<div class="abs brand">Renewpoint<br>Supply</div>
<nav class="abs nav">
  <a href="#" class="active">Home</a><a href="#">Services</a><a href="#">News</a><a href="#">Contact Us</a>
</nav>
<h1 class="abs hero-title">REUSABLE ELECTRONIC<br>OFFICE SUPPLIES</h1>
<p class="abs hero-text">We aim to provide all business with top quality of reused and environmentally friendly electronics, while maintaining a minimal impact on the natural environment.</p>
<a class="abs btn hero-btn">Shop
  <svg width="14" height="14" viewBox="0 0 14 14"><circle cx="7" cy="7" r="6.5" fill="#fff"/><path d="M6 4l3 3-3 3" stroke="#27a3e8" stroke-width="1.6" fill="none"/></svg>
</a>
<div class="abs dots"><span></span><span></span><span></span><span></span><span></span></div>

<!-- Decorative blobs -->
<div class="abs blob" style="left:-120px;top:760px;width:340px;height:360px"></div>
<div class="abs blob" style="left:880px;top:1120px;width:460px;height:640px;border-radius:46% 54% 50% 50%"></div>

<!-- Categories -->
<div class="abs cat" style="left:144px">
  <div class="cat-photo" role="img" aria-label="Photo of smartphones" style="background:linear-gradient(180deg,#2d6fa8 0%,#3a4fa0 50%,#7a2c8e 100%)"></div>
  <div class="cat-label">Smartphones</div>
</div>
<div class="abs cat" style="left:420px">
  <div class="cat-photo" role="img" aria-label="Photo of a laptop keyboard" style="background:linear-gradient(180deg,#a79aa7 0%,#8a6c95 50%,#6b2f8c 100%)"></div>
  <div class="cat-label">Laptops</div>
</div>
<div class="abs cat" style="left:700px">
  <div class="cat-photo" role="img" aria-label="Photo of a tablet on a desk" style="background:linear-gradient(180deg,#c9c3c9 0%,#9d7ea6 50%,#6a2d8c 100%)"></div>
  <div class="cat-label">Tablets</div>
</div>
<div class="abs cat" style="left:980px">
  <div class="cat-photo" role="img" aria-label="Photo of office gadgets" style="background:linear-gradient(180deg,#4a3b66 0%,#6b3b86 50%,#7a2c8e 100%)"></div>
  <div class="cat-label">Gadgets</div>
</div>

<!-- We are -->
<h2 class="abs we-title">WE ARE</h2>
<p class="abs we-sub">A smarter circular solution for electronic supplies</p>
<p class="abs we-text">Millions of devices are retired early each year while still fully capable. We collect, test and renew them so businesses can equip every desk for far less, keeping working hardware in use and out of landfill, with a clear warranty on every unit we supply.</p>
<div class="abs feature" style="top:1446px">
  <div class="feature-icon" style="background:var(--purple)">
    <svg width="26" height="26" viewBox="0 0 26 26" fill="none" stroke="#fff" stroke-width="2.4" stroke-linecap="round"><path d="M20 9a8 8 0 0 0-14-1"/><path d="M6 3v5h5"/><path d="M6 17a8 8 0 0 0 14 1"/><path d="M20 23v-5h-5"/></svg>
  </div>
  <div><h3>Buy reusable IT</h3><p>We specialise in renewed office devices at a fraction of the new price, each one tested, cleaned and backed by a lifetime warranty for your team.</p></div>
</div>
<div class="abs feature" style="top:1586px">
  <div class="feature-icon" style="background:#1f8ee0">$</div>
  <div><h3>Sell your IT Safely</h3><p>We can buy your used devices in bulk, wipe all data securely and turn equipment you no longer need into credit for your next order.</p></div>
</div>
<div class="abs device" style="left:665px;background:linear-gradient(160deg,#2b2f38,#0f1116 60%,#3a3f4a)" role="img" aria-label="Photo of a renewed smartphone, back view"></div>
<div class="abs device" style="left:880px;background:linear-gradient(170deg,#0c2a3a,#1c5a6a 45%,#0b1418)" role="img" aria-label="Photo of a renewed smartphone showing its home screen"></div>

<!-- Services -->
<h2 class="abs services-title">OUR SERVICES</h2>

<div class="abs service" style="left:160px;top:2136px">
  <svg class="service-icon" viewBox="0 0 150 150" aria-hidden="true">
    <circle cx="62" cy="78" r="62" fill="#f2c7de"/><circle cx="82" cy="70" r="56" fill="#cfe6f8"/>
    <circle cx="72" cy="75" r="52" fill="#5368d8"/>
    <path d="M52 62h22l18 18-22 22-18-18z" fill="none" stroke="#fff" stroke-width="4" stroke-linejoin="round"/><circle cx="61" cy="71" r="4" fill="#fff"/>
  </svg>
  <div><h3>Sale of renewed devices with lifetime warranty</h3><p>Every renewed device is fully tested and covered for life.</p><a class="btn read">Read more ›</a></div>
</div>

<div class="abs service" style="left:640px;top:2136px">
  <svg class="service-icon" viewBox="0 0 150 150" aria-hidden="true">
    <circle cx="62" cy="78" r="62" fill="#f2c7de"/><circle cx="82" cy="70" r="56" fill="#cfe6f8"/>
    <circle cx="72" cy="75" r="52" fill="#5368d8"/>
    <rect x="48" y="56" width="48" height="32" rx="3" fill="none" stroke="#fff" stroke-width="4"/><path d="M62 98h20M72 88v10" stroke="#fff" stroke-width="4"/>
  </svg>
  <div><h3>Purchase of old devices</h3><p>We buy your old office devices and give them a new life.</p><a class="btn read">Read more ›</a></div>
</div>

<div class="abs service" style="left:160px;top:2396px">
  <svg class="service-icon" viewBox="0 0 150 150" aria-hidden="true">
    <circle cx="62" cy="78" r="62" fill="#f2c7de"/><circle cx="82" cy="70" r="56" fill="#cfe6f8"/>
    <circle cx="72" cy="75" r="52" fill="#5368d8"/>
    <path d="M50 66h42l-9-9M94 84H52l9 9" fill="none" stroke="#fff" stroke-width="4" stroke-linecap="round" stroke-linejoin="round"/>
  </svg>
  <div><h3>Swap solution</h3><p>Buy from us and sell to us at once; we deduct your old devices from the total.</p><a class="btn read">Read more ›</a></div>
</div>

<div class="abs service" style="left:640px;top:2396px">
  <svg class="service-icon" viewBox="0 0 150 150" aria-hidden="true">
    <circle cx="62" cy="78" r="62" fill="#f2c7de"/><circle cx="82" cy="70" r="56" fill="#cfe6f8"/>
    <circle cx="72" cy="75" r="52" fill="#5368d8"/>
    <rect x="48" y="62" width="48" height="34" rx="4" fill="none" stroke="#fff" stroke-width="4"/><path d="M62 62v-7h20v7M48 76h48" stroke="#fff" stroke-width="4" fill="none"/>
  </svg>
  <div><h3>All Businesses</h3><p>We aim to provide all business with top quality of renewed and environmentally friendly electronics, while maintaining a minimal impact on the natural environment.</p><a class="btn read">Read more ›</a></div>
</div>

<!-- Footer -->
<svg class="abs footer-bg" viewBox="0 0 1200 468" aria-hidden="true">
  <path d="M0 40C260 0 520 10 760 40 950 64 1100 50 1200 20V468H0Z" fill="var(--blue)"/>
  <path d="M0 62C260 22 520 32 760 62 950 86 1100 72 1200 42V468H0Z" fill="var(--navy)"/>
</svg>
<div class="abs subscribe">SUBSCRIBE TO NEWSLETTER</div>
<div class="abs sub-form"><span>Enter Email</span><a class="btn">Subscribe
  <svg width="13" height="13" viewBox="0 0 14 14"><circle cx="7" cy="7" r="6.5" fill="#fff"/><path d="M6 4l3 3-3 3" stroke="#27a3e8" stroke-width="1.6" fill="none"/></svg></a></div>
<div class="abs social" aria-label="Social media links"><span></span><span></span><span></span><span></span><span></span></div>
<nav class="abs foot-nav"><a href="#">HOME</a><a href="#">SERVICES</a><a href="#">NEWS</a><a href="#">CONTACT US</a></nav>
<p class="abs copyright">Copyright © 2020, Renewpoint Supply All rights reserved &nbsp;|&nbsp; Privacy policy &nbsp;|&nbsp; Site Map &nbsp;|&nbsp; Disclaimer &nbsp;|&nbsp; Terms of use</p>

</body>
</html>
```